Lumoran signs for fridge and desk

I require 3 a4 designs very basic designs with single colour and easy to print. I have atached a style guide to see the fonts I used in my last three design. Please remember I'm printing in only one colour
PLease see the following link, of what I sell on quorbit. I will be selling this allong side these products.
https://www.quorbitshop.example/gp/item/K42H9XRDLM
Please see my competitors
https://www.quorbitshop.example/Planner-Magnetic-Calendar-Refrigerator-Container/dp/K7TQR2ZMWA/ref=sr_1_8?keywords=acrylic%2Bnote%2Bboard%2Brefrigerator%2Bdry%2Berase%2Bboard%2Bmagnetic%2Bclear&qid=1500000001&sr=8-8&th=1
and
https://www.quorbitshop.example/Magnetic-Acrylic-Calendar-Fridge-Refrigerator/dp/K9PWX4HNVE/ref=sr_1_4_sspa?keywords=acrylic+note+board+refrigerator+dry+erase+board+magnetic+clear&qid=1500000002&sr=8-4-spons&psc=1&spLa=UXhMbTNwZkRzWXZLcTJ3Rm5CaFRnSmRWZUx5UG1Sb1phSXVPY0F0TmJXa0dmWnNZeEhqUXJUbkxwVmRNZ0ViS2N5SXdBb0J1RnpQbVhoU2pOdFlxUmdDa1d2RHNMZUZuSHBaeEJtQ2tUZ1lqVnJRc0Vh
I'd like something more fun and different. But that can still be printed on Lumoran with one colour and be functional. A shopping list, a weekly planner(both that stick to a fridge) and a to do list that will sit on a desk or kitchen counter top.
PLease design
1st a4
Break into seven parts, with seven headings..... Monday to Sunday.... here customers will be able to write menus and upcoming events. I want this landcape
2nd a4
'Shopping List' is to be the heading
I want this landcape
3rd a4
'To Do List' is the only text I would like
I would like this portrat and lines marked and a check box on the left hand side
Remember I can only print on the acrylic with one colour. I want to be different from my competitors but I do want to be functional.
just a reminder. I can only print with one colour

```html
<!DOCTYPE html>
<html lang="en">
<head>
<meta charset="utf-8">
<title>Lumoran Weekly Planner</title>
<link rel="stylesheet" href="https://fonts.googleapis.com/css2?family=Kaushan+Script&display=swap">
<style>
  :root {
    --ink: #1c1c1c;
    --rule: #3a3a3a;
    --paper: #ffffff;
  }
  * { box-sizing: border-box; margin: 0; padding: 0; }
  html, body {
    width: 798px;
    height: 1200px;
    overflow: hidden;
    background: var(--paper);
  }
  .canvas {
    position: relative;
    width: 798px;
    height: 1200px;
  }
  .planner {
    position: absolute;
    left: 29px;
    top: 344px;
    width: 740px;
    height: 512px;
    border: 3px solid var(--ink);
    border-radius: 18px;
    background: var(--paper);
    display: flex;
    flex-direction: column;
    padding: 0 16px 0 14px;
  }
  .planner-title {
    height: 76px;
    display: flex;
    align-items: center;
    justify-content: center;
    font-family: "Kaushan Script", cursive;
    font-size: 50px;
    font-weight: 400;
    color: var(--ink);
    letter-spacing: -0.5px;
    border-bottom: 2px solid var(--rule);
    padding-top: 4px;
  }
  .day-list {
    list-style: none;
    flex: 1;
    display: flex;
    flex-direction: column;
  }
  .day-row {
    flex: 1;
    display: flex;
    align-items: center;
    border-bottom: 2px solid var(--rule);
  }
  .day-row:last-child { border-bottom: none; }
  .day-name {
    width: 144px;
    text-align: center;
    font-family: "Kaushan Script", cursive;
    font-size: 28px;
    color: var(--ink);
    letter-spacing: -0.3px;
  }
</style>
</head>
<body>
<main class="canvas">
  <section class="planner" aria-label="Weekly planner">
    <h1 class="planner-title">Weekly Planner</h1>
    <ul class="day-list">
      <li class="day-row"><span class="day-name">Sunday</span></li>
      <li class="day-row"><span class="day-name">Monday</span></li>
      <li class="day-row"><span class="day-name">Tuesday</span></li>
      <li class="day-row"><span class="day-name">Wednesday</span></li>
      <li class="day-row"><span class="day-name">Thursday</span></li>
      <li class="day-row"><span class="day-name">Friday</span></li>
      <li class="day-row"><span class="day-name">Saturday</span></li>
    </ul>
  </section>
</main>
</body>
</html>
```